Zerovan Medical

We are a medical supplier company we sell machines and equipment to all medical sectors in Iraq. Our services include not only the installation of these machines and equipment but also we provide support after installation and we train the staff to use these machines/equipment
We need a website that will make us stand out from our competitors, something professional and catchy
Starting from the home page, before showing the home page we want the loading screen to have our logo animated in a nice way
Then we can proceed to creating the other pages which are
Projects
Services
Training
About
and Contact us
Attached below is our logo and the color blue that we hope to use in the theme of the website
**** In the home page we want to focus on our partners and services****

Target Market(s)

Medical Sector

Industry/Entity Type

Medical

Coding

Coded - Design and coding required

Number of Pages Required

5+ page

Colors
0054AA
0677BA
7BADD7
CADEEF
E8F1F8

Requirements
Must have
• Animation in loading screen or animation in home page
Nice to have
• Some sort of animation for our partners

```html
<!DOCTYPE html>
<html lang="en">
<head>
<meta charset="utf-8">
<title>Zerovan Medical</title>
<link href="https://fonts.googleapis.com/css2?family=Poppins:wght@400;500;600;700&display=swap" rel="stylesheet">
<style>
:root{
  --blue-dark:#0054AA;
  --blue:#0677BA;
  --blue-mid:#7BADD7;
  --blue-soft:#CADEEF;
  --blue-pale:#E8F1F8;
  --ink:#111827;
  --text:#333a45;
  --white:#ffffff;
  --line:#c9ccd2;
}
*{box-sizing:border-box;margin:0;padding:0}
html,body{width:1200px;height:4320px;overflow:hidden}
body{font-family:'Poppins',sans-serif;color:var(--ink);background:var(--white);position:relative}
.abs{position:absolute}
.small{font-size:8.5px;line-height:16px;color:var(--text)}
.h2{font-size:41px;font-weight:600;letter-spacing:-0.5px;color:var(--ink)}
.accent{color:var(--blue)}
.btn{position:absolute;display:flex;align-items:center;justify-content:center;border-radius:20px;font-size:11px;font-weight:600}
.btn-solid{background:var(--blue-dark);color:var(--white)}
.btn-outline{background:var(--blue-soft);border:2px solid var(--blue);color:var(--blue-dark)}
.photo{position:absolute;border-radius:22px}

/* top bar */
.topbar{top:8px;left:505px;display:flex;gap:44px;font-size:8.5px;color:var(--ink)}
.topbar span{display:flex;align-items:center;gap:8px}
.topbar i{width:18px;height:18px;border:1.5px solid var(--blue);border-radius:50%;display:inline-block}
.nav-left{top:34px;left:0;width:168px;height:62px;background:var(--blue);border-radius:0 31px 31px 0}
.nav-right{top:34px;left:352px;width:848px;height:62px;background:var(--blue);border-radius:31px 0 0 31px}
.logo{display:flex;align-items:center;gap:7px;font-weight:600;font-size:13.5px;color:var(--blue-dark);white-space:nowrap}
.logo b{width:24px;height:24px;background:var(--blue);display:block;border-radius:3px}
.nav-links{top:56px;left:447px;display:flex;gap:32px;font-size:12px;font-weight:500;color:var(--white)}
.search{top:50px;left:980px;width:31px;height:31px;border-radius:50%;background:var(--blue-mid)}

/* services */
.services-band{top:1002px;left:0;width:1200px;height:491px;background:var(--blue)}
.svc{position:absolute;width:194px;height:168px;background:var(--white);border-radius:6px;text-align:center;padding-top:50px}
.svc h3{font-size:17px;font-weight:500;line-height:21px}
.svc p{font-size:8px;line-height:15px;color:var(--text);margin:10px 14px 0}
.svc-icon{position:absolute;top:-32px;left:65px;width:64px;height:64px;border-radius:50%;background:var(--white);box-shadow:0 3px 8px rgba(0,0,0,.12);display:flex;align-items:center;justify-content:center}

/* projects */
.proj{position:absolute;top:1706px;width:194px;height:275px;border:1.5px solid var(--line);border-radius:8px;background:var(--white)}
.proj .img{height:156px;border-radius:7px 7px 0 0}
.proj h3{font-size:18px;font-weight:500;margin:14px 0 0 21px}
.proj p{font-size:8px;line-height:16px;color:var(--text);margin:4px 20px 0 21px}
.proj.active{background:var(--blue);border-color:var(--blue)}
.proj.active h3,.proj.active p{color:var(--white)}
.arrow{position:absolute;left:80px;bottom:-17px;width:32px;height:32px;border-radius:50%;background:var(--blue-dark);display:flex;align-items:center;justify-content:center}
.proj.active .arrow{background:var(--blue-mid)}
.dots{top:2029px;left:548px;display:flex;gap:7px}
.dots i{width:8px;height:8px;border-radius:50%;background:var(--blue-soft);display:block}
.dots i.on{background:var(--blue-dark)}

/* products */
.products-band{top:2132px;left:0;width:1200px;height:1011px;background:var(--blue-pale)}
.prod{position:absolute;width:194px;height:255px;background:var(--white);border-radius:6px;text-align:center}
.prod .frame{position:absolute;top:26px;left:25px;width:144px;height:132px;border:1.5px solid #8d929a;border-radius:6px;display:flex;align-items:center;justify-content:center}
.prod .frame div{width:70px;height:90px;border-radius:10px}
.prod h3{position:absolute;top:175px;width:100%;font-size:15px;font-weight:500}
.prod .btn{top:209px;left:35px;width:122px;height:26px;font-size:10px;border-width:1.5px}
.page{position:absolute;top:3018px;width:32px;height:32px;border-radius:50%;border:1.5px solid var(--blue);display:flex;align-items:center;justify-content:center;font-size:14px;color:var(--blue-dark);background:var(--white)}
.page.on{background:var(--blue-dark);color:var(--white)}
.deco{position:absolute;border:1.5px solid var(--blue-mid);border-radius:50%;width:15px;height:15px}

/* quote */
.field{position:absolute;border:1.5px solid #9aa0a8;border-radius:7px;font-size:8.5px;color:var(--text);padding:12px 14px}

/* contact cards */
.footer{top:3880px;left:0;width:1200px;height:440px;background:var(--blue)}
.ccard{position:absolute;top:3793px;width:271px;height:174px;background:var(--blue-pale);border-radius:6px;text-align:center;padding-top:36px}
.ccard h4{font-size:15px;font-weight:500}
.ccard p{font-size:8px;line-height:16px;color:var(--text);margin:6px 30px 0}
.ccard .btn{left:70px;top:112px;width:130px;height:33px;border-width:1.5px}

.ft-head{font-size:15px;font-weight:500;color:var(--white)}
.ft-list{font-size:11px;line-height:27px;color:var(--white)}
.social{position:absolute;top:4138px;width:31px;height:31px;border-radius:50%;background:var(--white)}
.thumb{position:absolute;width:52px;height:45px;background:linear-gradient(135deg,#cfe0ee,#7fa3c2)}
</style>
</head>
<body>

<!-- header -->
<div class="abs topbar">
  <span><i></i>Lorem Ipsum is simply dummy text</span>
  <span><i></i>hello@zerovanmedical.com</span>
  <span><i></i>+964 7701234567</span>
</div>
<div class="abs nav-left"></div>
<div class="abs nav-right"></div>
<div class="abs logo" style="top:53px;left:188px"><b></b>Zerovan Medical</div>
<nav class="abs nav-links"><span>Home</span><span>Projects</span><span>Services</span><span>Training</span><span>About</span><span>Contact us</span></nav>
<div class="abs search">
  <svg width="31" height="31" viewBox="0 0 31 31"><circle cx="14" cy="14" r="5.5" fill="none" stroke="#fff" stroke-width="2"/><line x1="18" y1="18" x2="22" y2="22" stroke="#fff" stroke-width="2"/></svg>
</div>

<!-- hero -->
<h1 class="abs" style="top:226px;left:188px;font-size:34px;line-height:41px;font-weight:600;letter-spacing:-0.5px">Your Trusted Medical<br>Equipment <span class="accent">&amp; Machine</span><br><span class="accent">Supplier .</span></h1>
<p class="abs small" style="top:362px;left:188px">Lorem Ipsum is simply dummy text of the printing and typesetting industry.<br>Lorem Ipsum has been the industry's standard dummy text ever since the 1500s,</p>
<div class="btn btn-solid" style="top:425px;left:188px;width:124px;height:32px">Learn More</div>
<div class="photo" role="img" aria-label="Patient monitor on a stand in a hospital room" style="top:190px;left:592px;width:420px;height:313px;border-radius:60px 22px 22px 22px;background:linear-gradient(135deg,#dbe8f4,#8fb3d4 60%,#c7dbee)"></div>

<!-- about -->
<div class="photo" role="img" aria-label="Surgeon in scrubs working in an operating theatre" style="top:597px;left:188px;width:374px;height:311px;background:linear-gradient(135deg,#2b4f73,#5f89b3 55%,#1d3552)"></div>
<h2 class="abs h2" style="top:640px;left:630px">About <span class="accent">Us .</span></h2>
<p class="abs small" style="top:710px;left:630px;width:380px">Lorem Ipsum is simply dummy text of the printing and typesetting industry. Lorem Ipsum has been the industry's standard dummy text ever since the 1500s, when an unknown printer took a galley of type and scrambled it to make a type specimen book. It has survived not only five centuries, but also the leap into electronic typesetting, remaining essentially unchanged.</p>
<div class="btn btn-outline" style="top:816px;left:630px;width:185px;height:34px">Our Medical Services</div>
<div class="btn btn-solid" style="top:816px;left:830px;width:125px;height:34px">Learn More</div>

<!-- services -->
<div class="abs services-band"></div>
<h2 class="abs h2" style="top:1082px;left:0;width:1200px;text-align:center;color:var(--white)">Our Services .</h2>
<div class="svc" style="top:1190px;left:188px"><div class="svc-icon"><svg width="30" height="30"><circle cx="15" cy="15" r="10" fill="var(--blue-dark)"/></svg></div><h3>Trusted<br>Supplier</h3><p>Lorem Ipsum is simply dummy text of the printing and typesetting industry. Lorem Ipsum has been</p></div>
<div class="svc" style="top:1232px;left:397px"><div class="svc-icon"><svg width="30" height="30"><circle cx="15" cy="15" r="10" fill="var(--blue-dark)"/></svg></div><h3>Affordable<br>Pricing</h3><p>Lorem Ipsum is simply dummy text of the printing and typesetting industry. Lorem Ipsum has been</p></div>
<div class="svc" style="top:1190px;left:608px"><div class="svc-icon"><svg width="30" height="30"><circle cx="15" cy="15" r="10" fill="var(--blue-dark)"/></svg></div><h3>Original<br>Products</h3><p>Lorem Ipsum is simply dummy text of the printing and typesetting industry. Lorem Ipsum has been</p></div>
<div class="svc" style="top:1232px;left:818px"><div class="svc-icon"><svg width="30" height="30"><circle cx="15" cy="15" r="10" fill="var(--blue-dark)"/></svg></div><h3>Market<br>Reputation</h3><p>Lorem Ipsum is simply dummy text of the printing and typesetting industry. Lorem Ipsum has been</p></div>

<!-- projects -->
<h2 class="abs h2" style="top:1574px;left:188px">Our <span class="accent">Projects .</span></h2>
<p class="abs small" style="top:1642px;left:188px">Lorem Ipsum is simply dummy text of the printing and typesetting industry.<br>Lorem Ipsum has been the industry's standard dummy text ever since the 1500s,</p>
<div class="btn btn-outline" style="top:1612px;left:907px;width:105px;height:34px;border-width:1.5px">View All</div>

<div class="proj" style="left:188px"><div class="img" role="img" aria-label="Technician in protective suit at a machine" style="background:linear-gradient(135deg,#c9dced,#5f8fb8)"></div><h3>Lorem Ipsum</h3><p>Lorem Ipsum is simply dummy text of the printing and typesetting industry.</p><div class="arrow"><svg width="14" height="14"><path d="M4 10 L10 4 M5 4 H10 V9" stroke="#fff" stroke-width="1.5" fill="none"/></svg></div></div>
<div class="proj active" style="left:397px"><div class="img" role="img" aria-label="Laboratory bench with analysis equipment" style="background:linear-gradient(135deg,#e6eff7,#9dbbd6)"></div><h3>Lorem Ipsum</h3><p>Lorem Ipsum is simply dummy text of the printing and typesetting industry.</p><div class="arrow"><svg width="14" height="14"><path d="M4 10 L10 4 M5 4 H10 V9" stroke="#fff" stroke-width="1.5" fill="none"/></svg></div></div>
<div class="proj" style="left:608px"><div class="img" role="img" aria-label="Monitor and infusion stand in a ward" style="background:linear-gradient(135deg,#9bb3c9,#3e5d7c)"></div><h3>Lorem Ipsum</h3><p>Lorem Ipsum is simply dummy text of the printing and typesetting industry.</p><div class="arrow"><svg width="14" height="14"><path d="M4 10 L10 4 M5 4 H10 V9" stroke="#fff" stroke-width="1.5" fill="none"/></svg></div></div>
<div class="proj" style="left:818px"><div class="img" role="img" aria-label="Medical staff working in an operating room" style="background:linear-gradient(135deg,#b7cde0,#4a76a3)"></div><h3>Lorem Ipsum</h3><p>Lorem Ipsum is simply dummy text of the printing and typesetting industry.</p><div class="arrow"><svg width="14" height="14"><path d="M4 10 L10 4 M5 4 H10 V9" stroke="#fff" stroke-width="1.5" fill="none"/></svg></div></div>
<div class="abs dots"><i></i><i></i><i></i><i class="on"></i><i></i><i></i><i></i></div>

<!-- products -->
<div class="abs products-band"></div>
<div class="deco" style="top:2367px;left:98px"></div>
<div class="deco" style="top:2892px;left:1061px"></div>
<svg class="abs" style="top:2688px;left:114px" width="16" height="14"><polygon points="8,1 15,13 1,13" fill="none" stroke="#7BADD7" stroke-width="1.5"/></svg>
<svg class="abs" style="top:2375px;left:1087px" width="16" height="14"><polygon points="8,1 15,13 1,13" fill="none" stroke="#7BADD7" stroke-width="1.5"/></svg>
<h2 class="abs h2" style="top:2210px;left:0;width:1200px;text-align:center">Our Popular <span class="accent">Products .</span></h2>
<p class="abs small" style="top:2286px;left:0;width:1200px;text-align:center">Lorem Ipsum is simply dummy text of the printing and typesetting industry. Lorem Ipsum has<br>been the industry's standard dummy text ever since the 1500s,</p>
<div class="btn btn-solid" style="top:2348px;left:461px;width:129px;height:32px">Equipments</div>
<div class="btn btn-outline" style="top:2348px;left:607px;width:130px;height:32px;border-width:1.5px">Machines</div>

<div class="prod" style="top:2438px;left:188px"><div class="frame"><div role="img" aria-label="Hand sanitizer bottle" style="background:linear-gradient(#cfe6f5,#3b8ed0);width:34px"></div></div><h3>Hand Sanitizers</h3><div class="btn btn-outline">Buy Now</div></div>
<div class="prod" style="top:2438px;left:397px"><div class="frame"><div role="img" aria-label="KN95 mask" style="background:linear-gradient(#f4f4f4,#d9dbde);height:50px;width:80px"></div></div><h3>KN95 Masks</h3><div class="btn btn-outline">Buy Now</div></div>
<div class="prod" style="top:2438px;left:608px"><div class="frame"><div role="img" aria-label="Surgical gown" style="background:linear-gradient(#9cc4e6,#3f7fb8);width:44px"></div></div><h3>Gowns</h3><div class="btn btn-outline">Buy Now</div></div>
<div class="prod" style="top:2438px;left:818px"><div class="frame"><div role="img" aria-label="Blue three ply mask" style="background:linear-gradient(#a9d6f3,#4aa1dc);height:45px;width:84px"></div></div><h3>3-Ply Masks</h3><div class="btn btn-outline">Buy Now</div></div>
<div class="prod" style="top:2723px;left:188px"><div class="frame"><div role="img" aria-label="Black reusable mask" style="background:#1b1b1d;height:52px;width:80px"></div></div><h3>Reusable Masks</h3><div class="btn btn-outline">Buy Now</div></div>
<div class="prod" style="top:2723px;left:397px"><div class="frame"><div role="img" aria-label="Face shield" style="background:linear-gradient(#e8eef3,#c6d3de);width:56px;height:70px"></div></div><h3>Face Sheilds</h3><div class="btn btn-outline">Buy Now</div></div>
<div class="prod" style="top:2723px;left:608px"><div class="frame"><div role="img" aria-label="Blue nitrile gloves" style="background:linear-gradient(#a7cff0,#5a9fdb);width:64px;height:66px"></div></div><h3>Gloves</h3><div class="btn btn-outline">Buy Now</div></div>
<div class="prod" style="top:2723px;left:818px"><div class="frame"><div role="img" aria-label="Infrared thermometer" style="background:linear-gradient(#f4f5f7,#d5d8dc);width:44px"></div></div><h3>Thermometers</h3><div class="btn btn-outline">Buy Now</div></div>

<div class="page" style="left:540px">1</div>
<div class="page on" style="left:584px">2</div>
<div class="page" style="left:627px">3</div>

<!-- quote -->
<h2 class="abs h2" style="top:3220px;left:188px">Get A <span class="accent">Quote .</span></h2>
<p class="abs small" style="top:3290px;left:188px">Lorem Ipsum is simply dummy text of the printing and typesetting industry.<br>Lorem Ipsum has been the industry's standard dummy text ever since the 1500s,</p>
<div class="field" style="top:3355px;left:188px;width:194px;height:32px;padding-top:9px">Product Name</div>
<div class="field" style="top:3355px;left:397px;width:195px;height:32px;padding-top:9px">Company Name</div>
<div class="field" style="top:3405px;left:188px;width:194px;height:32px;padding-top:9px">Your Name</div>
<div class="field" style="top:3405px;left:397px;width:195px;height:32px;padding-top:9px">Your Phone</div>
<div class="field" style="top:3456px;left:188px;width:404px;height:32px;padding-top:9px">Subject</div>
<div class="field" style="top:3505px;left:188px;width:404px;height:123px">Message</div>
<div class="btn btn-solid" style="top:3665px;left:188px;width:105px;height:32px">Submit</div>
<div class="photo" role="img" aria-label="Doctor in a white coat checking a patient monitor" style="top:3256px;left:694px;width:318px;height:421px;border-radius:8px;background:linear-gradient(160deg,#3d5f70,#6f95a6 45%,#d8dfe3)"></div>

<!-- footer -->
<div class="abs footer"></div>
<div class="ccard" style="left:313px"><h4>hello@zerovanmedical.com</h4><p>Lorem Ipsum is simply dummy text of the printing and typesetting industry.</p><div class="btn btn-outline">Contact Us</div></div>
<div class="ccard" style="left:615px"><h4>+964 7701234567</h4><p>Lorem Ipsum is simply dummy text of the printing and typesetting industry.</p><div class="btn btn-outline">Contact Us</div></div>

<div class="abs logo" style="top:4048px;left:188px;color:var(--white)"><b style="background:var(--white)"></b>Zerovan Medical</div>
<p class="abs small" style="top:4088px;left:188px;color:var(--white)">Lorem Ipsum is simply dummy text of the<br>printing and typesetting industry.</p>
<div class="social" style="left:188px"></div>
<div class="social" style="left:234px"></div>
<div class="social" style="left:281px"></div>

<div class="abs" style="top:4040px;left:459px"><div class="ft-head">Quick Links</div><div class="ft-list">Home<br>Projects<br>Services<br>Training<br>About<br>Contact us</div></div>
<div class="abs" style="top:4040px;left:639px"><div class="ft-head">Services</div><div class="ft-list">Trusted Supplier<br>Affordable Pricing<br>Original Products<br>Market Reputation</div></div>
<div class="abs" style="top:4040px;left:841px"><div class="ft-head">Instagram</div></div>
<div class="thumb" role="img" aria-label="Clinic photo" style="top:4071px;left:841px"></div>
<div class="thumb" role="img" aria-label="Clinic photo" style="top:4071px;left:902px"></div>
<div class="thumb" role="img" aria-label="Clinic photo" style="top:4071px;left:962px"></div>
<div class="thumb" role="img" aria-label="Clinic photo" style="top:4126px;left:841px"></div>
<div class="thumb" role="img" aria-label="Clinic photo" style="top:4126px;left:902px"></div>
<div class="thumb" role="img" aria-label="Clinic photo" style="top:4126px;left:962px"></div>

<div class="abs" style="top:4284px;left:188px;width:824px;height:1px;background:rgba(255,255,255,.5)"></div>
<p class="abs" style="top:4294px;left:0;width:1200px;text-align:center;font-size:8.5px;color:var(--white)">Copyright - <b>Zerovan Medical</b> All Rights Reserved.</p>

</body>
</html>
```